Yummy Website Re-Design

We have a good website but no VERY GOOD :)

We would like improve the user experience, in shopping page particularly.

Target Market(s)

people 25-40 70% of girl (actually)

Industry/Entity Type

Shopping

Requirements
Must have
• Redesign of www.brunolake.ch
Same colors
Same logotype

1) Homepage
- With highlight product / offer (large display!)
- Space to explain the concept
- Delicious button call-to-action for order a breakfast

2) THE CONCEPT
- Page for explain the concept and team pictures (3persons)

3) COMPOSE !
- Shopping page with, on the top, the X package we offer (business pack, st valentine, christmas, family, etc.) (slider?)

- Then, the products (grid?) classified into categories, we would'like to display one photo / item, the name, the weight and the price.

If you want to add the product, you must choose the number of elements and add to cart

Please, suscribe and test the order process to view all step

4) DELIVERY ZONES
- Page with map of different delivery rate and possibility

5) FAQ

X) Footer with the same information what www.brunolake.ch

Yummy, delicious design (we delivery very delicious breakfast @home).

LET'S EXPLODE YOUR CREATIVITY WITH THIS WORDS : YUMMY, DELICIOUS, SWEET.

```html
<!DOCTYPE html>
<html lang="en">
<head>
<meta charset="utf-8">
<title>Lake Tray – Breakfast in bed, Geneva</title>
<link href="https://fonts.googleapis.com/css2?family=Bree+Serif&family=Dancing+Script:wght@600&family=Lora:ital,wght@0,400;0,600;1,400&family=Uncial+Antiqua&family=Varela+Round&display=swap" rel="stylesheet">
<style>
:root{
  --peach:#fcd3a6;
  --peach-light:#fde4c6;
  --band:#4a2e16;
  --cocoa:#7a5f47;
  --cocoa-dark:#3a2512;
  --footer:#381c0b;
  --cream:#f3ead7;
  --cream-dark:#e2d4b6;
  --ink:#3d2614;
  --olive:#a9a060;
  --orange:#c8781c;
  --gold:#f5a21a;
  --nav-text:#cdb08a;
}
*{margin:0;padding:0;box-sizing:border-box}
html,body{width:1200px;height:2184px;overflow:hidden}
body{position:relative;background:var(--cocoa);font-family:"Lora",Georgia,serif;color:var(--ink)}
.abs{position:absolute}

/* header */
.header{left:0;top:0;width:1200px;height:503px;background:linear-gradient(var(--peach-light),var(--peach))}
.header-ornament{top:48px;width:290px;height:64px;border-radius:32px;background:linear-gradient(90deg,rgba(214,150,90,.2),rgba(214,150,90,.4),rgba(214,150,90,.2))}
.header-ornament.left{left:140px}
.header-ornament.right{left:770px}
.brand{left:0;top:58px;width:1200px;text-align:center;font-family:"Lora",serif;font-weight:600;font-size:62px;color:#9a6a44;letter-spacing:1px}
.brand-dot{display:inline-block;width:14px;height:14px;border-radius:50%;background:#9a6a44;margin-left:10px;vertical-align:middle}

.nav{left:0;top:188px;width:1200px;height:63px;background:var(--band);border-top:3px dashed #6a4826;border-bottom:3px dashed #6a4826}
.nav a{position:absolute;top:18px;transform:translateX(-50%);font-family:"Lora",serif;font-size:17px;color:var(--nav-text);text-decoration:none;letter-spacing:.5px;white-space:nowrap}
.nav a.active{color:#fff}

.texture{left:0;top:503px;width:1200px;height:1330px;background:repeating-linear-gradient(0deg,rgba(0,0,0,.03) 0 2px,transparent 2px 4px),var(--cocoa)}

/* hero */
.tagline{left:143px;top:288px;font-family:"Uncial Antiqua",serif;font-size:36px;line-height:52px;color:var(--ink)}
.chef{left:183px;top:463px;width:119px;height:135px;border-radius:10px 10px 0 0;background:linear-gradient(180deg,#e7a48c 0%,#eed6c4 55%,#f1e4d6 100%)}
.order-btn{left:143px;top:595px;width:201px;height:90px;border-radius:6px;background:linear-gradient(#d8904a,#b8692a);box-shadow:0 6px 8px rgba(0,0,0,.35);font-family:"Bree Serif",serif;font-size:21px;line-height:24px;color:#fff;text-align:center;padding-top:9px;letter-spacing:2px}
.slider-frame{left:368px;top:266px}
.slide-photo{left:380px;top:282px;width:665px;height:440px;border-radius:50%;background:radial-gradient(ellipse at 30% 60%,#c89a62 0 22%,transparent 40%),radial-gradient(ellipse at 72% 55%,#e9c7a3 0 18%,transparent 34%),linear-gradient(#f6efe2,#eadfcb)}
.slide-arrow{width:44px;height:44px;background:#2a1708}
.dots span{position:absolute;top:0;width:16px;height:16px;border-radius:50%;background:#8a7462}
.dots span.on{background:#fff}

/* welcome */
.welcome{left:141px;top:786px;width:918px;height:311px;border-radius:8px;background:linear-gradient(90deg,var(--cream-dark),var(--cream) 20%,var(--cream) 80%,var(--cream-dark))}
.welcome h1{position:absolute;left:0;top:10px;width:100%;text-align:center;font-family:"Dancing Script",cursive;font-weight:600;font-size:54px;color:#6a4423}
.welcome .copy{position:absolute;left:88px;top:86px;width:750px;font-style:italic;font-size:17px;line-height:20px;color:#2d1a0c}
.welcome .copy p{margin-bottom:20px}

/* gallery */
.gallery-title{left:141px;top:1146px;width:646px;text-align:center;font-size:22px;color:#f1e3cc;letter-spacing:.5px}
.gallery-title span{background:var(--cocoa);padding:0 16px;position:relative}
.gallery-rule{left:141px;top:1160px;width:646px;border-top:1px dashed #b59c82}
.product{width:176px;height:176px;border-radius:50%;border:5px solid #fff;box-shadow:0 6px 10px rgba(0,0,0,.35)}
.weekly{left:817px;top:1147px;width:242px;height:240px;border:5px solid #fff;border-radius:8px;background:radial-gradient(circle at 55% 35%,#f0e2cc 0 25%,#b64a2b 50%,#5a2012);overflow:hidden}
.weekly-label{left:817px;top:1317px;width:242px;height:58px;background:var(--orange);font-family:"Dancing Script",cursive;font-weight:600;font-size:36px;color:#fff;text-align:center;line-height:58px}

/* steps */
.steps{left:141px;top:1476px;width:918px;height:298px;border-radius:8px;background:var(--cocoa-dark);box-shadow:0 6px 10px rgba(0,0,0,.3)}
.ribbon-title{left:274px;top:1438px;width:677px;height:72px;background:linear-gradient(#f7f0e1,#e3d6bc);text-align:center;font-family:"Bree Serif",serif;font-size:27px;color:var(--ink);line-height:72px}
.ribbon-badge{display:inline-block;width:44px;height:44px;line-height:44px;border-radius:50%;background:var(--olive);color:#fff;margin:0 8px;vertical-align:middle}
.step-circle{width:118px;height:118px;border-radius:50%;background:var(--cream);border:4px solid #d8ccb0}
.step-num{width:58px;height:58px;border-radius:50%;background:var(--olive);border:4px solid var(--cream);font-family:"Bree Serif",serif;font-size:28px;color:#fff;text-align:center;line-height:50px}
.step-label{width:240px;transform:translateX(-50%);top:1686px;text-align:center;font-family:"Bree Serif",serif;font-size:20px;line-height:28px;color:var(--cream)}

/* footer */
.footer{left:0;top:1833px;width:1200px;height:236px;background:var(--footer)}
.footer h3{position:absolute;top:20px;transform:translateX(-50%);font-family:"Bree Serif",serif;font-weight:400;font-size:21px;color:#fff;white-space:nowrap}
.footer p{position:absolute;transform:translateX(-50%);text-align:center;font-family:"Varela Round",sans-serif;font-size:12.5px;line-height:20px;color:#eadccb}
.card{position:absolute;top:73px;width:40px;height:26px;border-radius:3px}
.field{position:absolute;left:834px;width:223px;height:33px;background:#4a2d18;border-radius:2px;font-family:"Varela Round",sans-serif;font-size:12.5px;color:#eadccb;line-height:33px;padding-left:14px}
.subscribe{position:absolute;left:891px;top:146px;width:111px;height:33px;background:var(--gold);border:1px solid #fff3c9;font-family:"Bree Serif",serif;font-size:17px;color:#2a1708;text-align:center;line-height:31px}

.bottom-links{left:0;top:2078px;width:1200px;text-align:center;font-family:"Varela Round",sans-serif;font-size:14px;color:#2a1708;line-height:20px}
.bottom-links span{margin:0 10px}
.social{top:2127px;width:44px;height:44px;border-radius:50%;background:#3a2210}
</style>
</head>
<body>

<div class="abs header"></div>
<div class="abs header-ornament left" role="img" aria-label="Decorative swirl ornament"></div>
<div class="abs header-ornament right" role="img" aria-label="Decorative swirl ornament"></div>
<div class="abs brand">Lake Tray<span class="brand-dot"></span></div>

<nav class="abs nav">
  <a class="active" style="left:230px">HOME</a>
  <a style="left:406px">THE CONCEPT</a>
  <a style="left:598px">COMPOSE</a>
  <a style="left:801px">DILIVERY ZONES</a>
  <a style="left:980px">FAQ</a>
</nav>

<div class="abs texture"></div>

<!-- hero -->
<div class="abs tagline">YUMMY<br>DELICIOUS<br>SWEET</div>
<div class="abs chef" role="img" aria-label="Smiling chef in a red hat and white jacket"></div>
<div class="abs order-btn">ORDER<br>A<br>BREAKFAST</div>

<div class="abs slide-photo" role="img" aria-label="Bread basket and a bowl of soup on a breakfast table"></div>
<svg class="abs slider-frame" width="692" height="470" viewBox="0 0 692 470" aria-hidden="true">
  <ellipse cx="346" cy="235" rx="336" ry="225" fill="none" stroke="#3a2210" stroke-width="12"/>
  <path d="M180 40 Q330 -10 540 30" fill="none" stroke="#3a2210" stroke-width="8" stroke-linecap="round"/>
</svg>
<svg class="abs slide-arrow" style="left:375px;top:499px" viewBox="0 0 44 44"><path d="M26 12 L16 22 L26 32" fill="none" stroke="#fff" stroke-width="3"/></svg>
<svg class="abs slide-arrow" style="left:1004px;top:499px" viewBox="0 0 44 44"><path d="M18 12 L28 22 L18 32" fill="none" stroke="#fff" stroke-width="3"/></svg>
<div class="abs dots" style="left:725px;top:716px">
  <span class="on" style="left:0"></span><span style="left:22px"></span><span style="left:44px"></span>
</div>

<!-- welcome -->
<section class="abs welcome">
  <h1>Welcome to Lake Tray</h1>
  <div class="copy">
    <p>We are a company from Geneva, the first and only to offer to bring you the best buffet breakfast in bed.</p>
    <p>Whether you have guests, a large family or just your lover, love to treat or impress, we are at your disposal!</p>
    <p>Amazing cakes, crispy croissants, chocolate lollipops to get up at night, in short, a better breakfast than hotel, delivered to your door as you wish!</p>
    <p>Find out more about our offer on the page FAQ or place an order now!</p>
  </div>
</section>

<!-- gallery -->
<div class="abs gallery-rule"></div>
<div class="abs gallery-title"><span>PRODUCT GALLERY</span></div>
<svg class="abs" style="left:138px;top:1255px" width="24" height="70" viewBox="0 0 24 70"><path d="M20 2 L4 35 L20 68" fill="none" stroke="#c9b49c" stroke-width="2"/></svg>
<svg class="abs" style="left:766px;top:1255px" width="24" height="70" viewBox="0 0 24 70"><path d="M4 2 L20 35 L4 68" fill="none" stroke="#c9b49c" stroke-width="2"/></svg>
<div class="abs product" style="left:183px;top:1202px;background:radial-gradient(circle at 50% 45%,#d9b48a,#6a4222)" role="img" aria-label="Assorted bread rolls"></div>
<div class="abs product" style="left:375px;top:1202px;background:radial-gradient(circle at 50% 45%,#f0c27a,#8a5a2a)" role="img" aria-label="Golden puff pastries"></div>
<div class="abs product" style="left:570px;top:1202px;background:radial-gradient(circle at 50% 45%,#f2c98a,#a8763e)" role="img" aria-label="Small jam tartlets"></div>
<div class="abs weekly" role="img" aria-label="Cup of hot chocolate with a heart cookie"></div>
<div class="abs weekly-label">Weekly Special</div>

<!-- steps -->
<section class="abs steps"></section>
<div class="abs ribbon-title">ORDER YOUR LAKE TRAY IN<span class="ribbon-badge">4</span>STEPS</div>

<div class="abs step-circle" style="left:179px;top:1545px"></div>
<div class="abs step-circle" style="left:413px;top:1545px"></div>
<div class="abs step-circle" style="left:645px;top:1545px"></div>
<div class="abs step-circle" style="left:877px;top:1545px"></div>

<svg class="abs" style="left:210px;top:1580px" width="56" height="48" viewBox="0 0 56 48" aria-label="Cup icon"><path d="M8 10 H40 V26 Q40 36 24 36 Q8 36 8 26 Z" fill="#8e7a3e"/><path d="M40 14 Q50 14 50 20 Q50 26 40 26" fill="none" stroke="#8e7a3e" stroke-width="4"/><rect x="2" y="40" width="48" height="4" rx="2" fill="#8e7a3e"/></svg>
<svg class="abs" style="left:446px;top:1580px" width="52" height="48" viewBox="0 0 52 48" aria-label="Cart icon"><path d="M2 6 H10 L16 32 H42 L48 12 H12" fill="none" stroke="#8e7a3e" stroke-width="4" stroke-linejoin="round"/><circle cx="19" cy="40" r="4" fill="#8e7a3e"/><circle cx="38" cy="40" r="4" fill="#8e7a3e"/></svg>
<svg class="abs" style="left:680px;top:1585px" width="50" height="36" viewBox="0 0 50 36" aria-label="Payment card icon"><rect x="1" y="1" width="48" height="34" rx="4" fill="#8e7a3e"/><rect x="1" y="9" width="48" height="6" fill="#efe4cd"/><rect x="6" y="24" width="14" height="4" fill="#efe4cd"/></svg>
<svg class="abs" style="left:906px;top:1578px" width="60" height="48" viewBox="0 0 60 48" aria-label="Bicycle icon"><circle cx="12" cy="34" r="10" fill="none" stroke="#8e7a3e" stroke-width="3"/><circle cx="48" cy="34" r="10" fill="none" stroke="#8e7a3e" stroke-width="3"/><path d="M12 34 L24 20 L38 20 L48 34 M24 20 L30 34 L38 20" fill="none" stroke="#8e7a3e" stroke-width="3"/><circle cx="34" cy="7" r="5" fill="#8e7a3e"/></svg>

<svg class="abs" style="left:305px;top:1572px" width="820" height="60" viewBox="0 0 820 60" aria-hidden="true">
  <g fill="none" stroke="#7a6450" stroke-width="1.5" stroke-dasharray="4 4">
    <path d="M0 32 H60"/><path d="M52 10 L72 32 L52 54" stroke-dasharray="none"/>
    <path d="M232 32 H292"/><path d="M284 10 L304 32 L284 54" stroke-dasharray="none"/>
    <path d="M464 32 H524"/><path d="M516 10 L536 32 L516 54" stroke-dasharray="none"/>
  </g>
</svg>

<div class="abs step-num" style="left:270px;top:1617px">1</div>
<div class="abs step-num" style="left:500px;top:1617px">2</div>
<div class="abs step-num" style="left:732px;top:1617px">3</div>
<div class="abs step-num" style="left:964px;top:1617px">4</div>

<div class="abs step-label" style="left:244px">Prepare<br>your Lake Tray</div>
<div class="abs step-label" style="left:476px">Choose the date &amp;<br>time of delivery</div>
<div class="abs step-label" style="left:708px">Select the<br>payment method</div>
<div class="abs step-label" style="left:940px">Enjoy!</div>

<!-- footer -->
<footer class="abs footer">
  <h3 style="left:278px">Secure Payment</h3>
  <div class="card" style="left:168px;background:#dfe8f3"></div>
  <div class="card" style="left:214px;background:#e5a03c"></div>
  <div class="card" style="left:260px;background:#2a4f9c"></div>
  <div class="card" style="left:306px;background:#3f7fb8"></div>
  <div class="card" style="left:352px;background:#f2d23a"></div>
  <p style="left:278px;top:130px;width:250px">Quickly and easily pay your order by credit card secure platform with PayNest. We accept payment by Versa, Meridian Card or Atlas Express.</p>

  <h3 style="left:626px">Delivery Throughout Geneva</h3>
  <svg style="position:absolute;left:584px;top:62px" width="96" height="48" viewBox="0 0 96 48" aria-label="Delivery truck icon">
    <rect x="30" y="2" width="64" height="32" fill="#fff"/>
    <path d="M2 34 V18 L10 8 H26 V34 Z" fill="#fff"/>
    <rect x="2" y="34" width="92" height="4" fill="#fff"/>
    <circle cx="16" cy="40" r="6" fill="#fff" stroke="#381c0b" stroke-width="2"/>
    <circle cx="76" cy="40" r="6" fill="#fff" stroke="#381c0b" stroke-width="2"/>
  </svg>
  <p style="left:626px;top:133px;width:270px">Delivery from 4 CHF, see our prices on our different delivery! More</p>

  <h3 style="left:946px">Our Newsletter!</h3>
  <div class="field" style="top:66px">Enter Your Name</div>
  <div class="field" style="top:106px">Enter Your Email</div>
  <div class="subscribe">SUBSCRIBE</div>
</footer>

<div class="abs bottom-links">
  Home<span>|</span>The Concept<span>|</span>Compose<span>|</span>Dilivery Zones<span>|</span>FAQ<br>
  Copyright ©2012 Lake Tray. All Rights Reserved
</div>
<div class="abs social" style="left:567px" role="img" aria-label="Social network link"></div>
<div class="abs social" style="left:618px" role="img" aria-label="Social network link"></div>

</body>
</html>
```